UK Supplement Company Needs a Label for Diet Protein Powder

We need a new, modern and fresh design for our Diet Protein Powder. Our protein powder is packaged in black plastic tubs (photo attached) and needs an attractive label. We would like to see designs that grab attention and look professional. We're very open to ideas. The label should be 88mm x 365mm. We also prefer PSD format where possible. These alterations could be made once your design is chosen. Have attached photo of our shake ingredients/benefits.
Updates

Need extra days to review

Target Market(s)

Slimmers

Industry/Entity Type

Health And Wellness

Font styles to use
Serif
Sans Serif

Colors

Designer to choose colors to be used in the design.

Requirements
Must have
• Clean, Modern and Professional Look. Eye catching. The flavour, we offer 6 flavours so this must be something we can edit (Flavours are Banana, Chocolate, Chocolate Mint, Strawberry, Toffee and Vanilla).
Nice to have
• Our logo, this can be KALVO Nutrition or just KALVO. Our logo files are attached.
Should not have
• We do not want to see people (faces or bodies) on the design.

```html
<!DOCTYPE html>
<html lang="en">
<head>
<meta charset="UTF-8">
<title>KALVO Nutrition – Low Calorie Protein Shake Labels</title>
<link href="https://fonts.googleapis.com/css2?family=Signika:wght@400;600;700&family=Raleway:wght@500;600&display=swap" rel="stylesheet">
<style>
  :root {
    --page: #ffffff;
    --band-grey: #56595c;
    --band-grey-dark: #45484b;
    --tab-grey: #4a4d50;
    --white: #ffffff;
    --ink: #1e1e1e;
    --strawberry: #d4232f;
    --strawberry-dark: #a5151e;
    --strawberry-tint: #f9d6d8;
    --strawberry-photo-a: #e8434a;
    --strawberry-photo-b: #b3121c;
    --chocolate: #5b2c1d;
    --chocolate-dark: #3e1c11;
    --chocolate-tint: #efd6cc;
    --chocolate-photo-a: #6e3a26;
    --chocolate-photo-b: #3b1c11;
  }
  * { box-sizing: border-box; margin: 0; padding: 0; }
  html, body {
    width: 1200px; height: 800px; overflow: hidden;
    background: var(--page);
  }
  .canvas { position: relative; width: 1200px; height: 800px; }
  .label {
    position: absolute; top: 160px;
    width: 540px; height: 480px;
    overflow: hidden;
    background: var(--white);
    font-family: 'Signika', sans-serif;
  }
  .label--strawberry {
    left: 30px;
    --accent: var(--strawberry);
    --accent-dark: var(--strawberry-dark);
    --accent-tint: var(--strawberry-tint);
    --photo-a: var(--strawberry-photo-a);
    --photo-b: var(--strawberry-photo-b);
  }
  .label--chocolate {
    left: 630px;
    --accent: var(--chocolate);
    --accent-dark: var(--chocolate-dark);
    --accent-tint: var(--chocolate-tint);
    --photo-a: var(--chocolate-photo-a);
    --photo-b: var(--chocolate-photo-b);
  }
  .label__top-band {
    position: absolute; left: 0; top: 0; width: 100%; height: 8px;
    background: var(--accent);
  }
  .label__header {
    position: absolute; left: 0; top: 8px; width: 100%; height: 206px;
    background: linear-gradient(90deg, var(--band-grey-dark), var(--band-grey) 50%, var(--band-grey-dark));
  }
  .flavour-tab {
    position: absolute; left: 50%; top: 0; transform: translateX(-50%);
    width: 112px; height: 36px;
    color: var(--white); text-align: center;
  }
  .flavour-tab svg { position: absolute; inset: 0; }
  .flavour-tab__name {
    position: relative; display: block; padding-top: 6px;
    font-family: 'Raleway', sans-serif; font-weight: 500;
    font-size: 10px; letter-spacing: 0.5px; line-height: 11px;
  }
  .flavour-tab__word {
    position: relative; display: block;
    font-weight: 600; font-size: 14px; letter-spacing: 1px; line-height: 14px;
  }
  .brand {
    position: absolute; left: 0; top: 62px; width: 100%;
    text-align: center; color: var(--white); font-weight: 600;
  }
  .brand__name { display: block; font-size: 56px; line-height: 56px; letter-spacing: 1px; }
  .brand__sub { display: block; font-size: 10px; letter-spacing: 8px; margin-top: 6px; padding-left: 8px; }
  .label__fade {
    position: absolute; left: 0; top: 360px; width: 100%; height: 110px;
    background: linear-gradient(180deg, var(--white), var(--accent-tint) 70%, var(--accent));
  }
  .bowl {
    position: absolute; left: 136px; top: 214px; width: 268px; height: 56px;
  }
  .flavour-photo {
    position: absolute; left: 200px; top: 150px; width: 140px; height: 96px;
    border-radius: 46% 46% 40% 40%;
    background: radial-gradient(ellipse at 45% 40%, var(--photo-a), var(--photo-b));
  }
  .claim {
    position: absolute; left: 0; top: 276px; width: 100%;
    text-align: center; color: var(--ink);
    font-family: 'Raleway', sans-serif; font-weight: 500; font-size: 23px;
  }
  .rule {
    position: absolute; left: 50%; transform: translateX(-50%);
    width: 310px; height: 1px; background: var(--accent);
  }
  .rule--top { top: 310px; }
  .rule--bottom { top: 362px; }
  .product {
    position: absolute; left: 0; top: 314px; width: 100%;
    text-align: center; color: var(--accent);
    font-weight: 700; font-size: 38px; letter-spacing: 0.5px; line-height: 46px;
  }
  .nutrition {
    position: absolute; left: 50%; top: 384px; transform: translateX(-50%);
    width: 76px; text-align: center;
  }
  .nutrition__grid {
    display: flex; border: 1px solid var(--ink); background: var(--white); height: 28px;
  }
  .nutrition__cell { flex: 1; line-height: 1; padding-top: 3px; color: var(--ink); }
  .nutrition__cell + .nutrition__cell { border-left: 1px dashed var(--accent); }
  .nutrition__value { display: block; font-size: 16px; font-weight: 600; }
  .nutrition__unit { display: block; font-size: 5px; font-weight: 600; margin-top: 1px; }
  .nutrition__serving {
    background: var(--accent); color: var(--white);
    font-family: 'Raleway', sans-serif; font-size: 8px; line-height: 11px;
  }
  .label__bottom-band {
    position: absolute; left: 0; top: 466px; width: 100%; height: 14px;
    background: var(--accent-dark);
  }
  .supplement-tab {
    position: absolute; left: 50%; top: 456px; transform: translateX(-50%);
    width: 134px; height: 24px; color: var(--white); text-align: center;
  }
  .supplement-tab svg { position: absolute; inset: 0; }
  .supplement-tab span {
    position: relative; display: block; line-height: 24px;
    font-family: 'Raleway', sans-serif; font-weight: 600; font-size: 9.5px; letter-spacing: 0.3px;
  }
</style>
</head>
<body>
<main class="canvas">

  <section class="label label--strawberry">
    <div class="label__top-band"></div>
    <div class="label__header" role="img" aria-label="Dark grey band with fine zig-zag line texture"></div>
    <div class="flavour-tab">
      <svg viewBox="0 0 112 36" preserveAspectRatio="none" aria-hidden="true"><polygon points="0,0 112,0 104,36 8,36" fill="var(--accent)"/></svg>
      <span class="flavour-tab__name">STRAWBERRY</span>
      <span class="flavour-tab__word">FLAVOUR</span>
    </div>
    <div class="brand">
      <span class="brand__name">KALVO</span>
      <span class="brand__sub">NUTRITION</span>
    </div>
    <div class="label__fade"></div>
    <svg class="bowl" viewBox="0 0 268 56" aria-hidden="true">
      <path d="M0,0 H268 C250,38 200,56 134,56 C68,56 18,38 0,0 Z" fill="var(--accent)"/>
      <path d="M22,0 H246 C226,26 186,40 134,40 C82,40 42,26 22,0 Z" fill="var(--accent-dark)"/>
    </svg>
    <div class="flavour-photo" role="img" aria-label="Photo of fresh ripe strawberries"></div>
    <p class="claim">LOW CALORIE</p>
    <div class="rule rule--top"></div>
    <h2 class="product">PROTEIN SHAKE</h2>
    <div class="rule rule--bottom"></div>
    <div class="nutrition">
      <div class="nutrition__grid">
        <div class="nutrition__cell"><span class="nutrition__value">117</span><span class="nutrition__unit">CALORIES</span></div>
        <div class="nutrition__cell"><span class="nutrition__value">4.2</span><span class="nutrition__unit">CARBS</span></div>
      </div>
      <div class="nutrition__serving">PER SERVING</div>
    </div>
    <div class="label__bottom-band"></div>
    <div class="supplement-tab">
      <svg viewBox="0 0 134 24" preserveAspectRatio="none" aria-hidden="true"><polygon points="8,0 126,0 134,24 0,24" fill="var(--tab-grey)"/></svg>
      <span>DIETARY SUPPLEMENT</span>
    </div>
  </section>

  <section class="label label--chocolate">
    <div class="label__top-band"></div>
    <div class="label__header" role="img" aria-label="Dark grey band with fine zig-zag line texture"></div>
    <div class="flavour-tab">
      <svg viewBox="0 0 112 36" preserveAspectRatio="none" aria-hidden="true"><polygon points="0,0 112,0 104,36 8,36" fill="var(--accent)"/></svg>
      <span class="flavour-tab__name">CHOCOLATE</span>
      <span class="flavour-tab__word">FLAVOUR</span>
    </div>
    <div class="brand">
      <span class="brand__name">KALVO</span>
      <span class="brand__sub">NUTRITION</span>
    </div>
    <div class="label__fade"></div>
    <svg class="bowl" viewBox="0 0 268 56" aria-hidden="true">
      <path d="M0,0 H268 C250,38 200,56 134,56 C68,56 18,38 0,0 Z" fill="var(--accent)"/>
      <path d="M22,0 H246 C226,26 186,40 134,40 C82,40 42,26 22,0 Z" fill="var(--accent-dark)"/>
    </svg>
    <div class="flavour-photo" role="img" aria-label="Photo of stacked dark chocolate bar pieces"></div>
    <p class="claim">LOW CALORIE</p>
    <div class="rule rule--top"></div>
    <h2 class="product">PROTEIN SHAKE</h2>
    <div class="rule rule--bottom"></div>
    <div class="nutrition">
      <div class="nutrition__grid">
        <div class="nutrition__cell"><span class="nutrition__value">117</span><span class="nutrition__unit">CALORIES</span></div>
        <div class="nutrition__cell"><span class="nutrition__value">4.2</span><span class="nutrition__unit">CARBS</span></div>
      </div>
      <div class="nutrition__serving">PER SERVING</div>
    </div>
    <div class="label__bottom-band"></div>
    <div class="supplement-tab">
      <svg viewBox="0 0 134 24" preserveAspectRatio="none" aria-hidden="true"><polygon points="8,0 126,0 134,24 0,24" fill="var(--tab-grey)"/></svg>
      <span>DIETARY SUPPLEMENT</span>
    </div>
  </section>

</main>
</body>
</html>
```